New Zealand Luggage Importer Needs Business Cards

We need professional, creative and fashionable business cards created.
We are based in New Zealand and import and distribute high-end, quality, fashionable and durable luggage.
We pride ourselves on selling the very best quality luggage, second only to 1 brand (which we won't mention here)...we use the same manufacturer. However, our prices are much more reasonable.
Business
Sam Ortiz
027 481 2956
3/17 Kestrel Lane, Morrow Flats, Auckland, 0614
PO Box 208354, North Shore, Auckland 0792
09-527-3061
sales@brindlecases.co.nz / www.brindlecases.co.nz

```html
<!DOCTYPE html>
<html lang="en">
<head>
<meta charset="utf-8">
<title>Brindle Cases – Business Card</title>
<link href="https://fonts.googleapis.com/css2?family=Source+Sans+3:wght@400;600;700&display=swap" rel="stylesheet">
<style>
  :root {
    --backdrop: #d9d9d6;
    --panel-dark: #3c3e41;
    --panel-dark-edge: #55585b;
    --frost: #eeeeec;
    --frost-shade: #d6d7d6;
    --gold: #c9a54a;
    --gold-light: #e2c776;
    --gold-deep: #8f7230;
    --ink-light: #e6e6e4;
    --ink-dark: #2a2b2d;
    --gold-text: #f3e7c2;
  }
  html, body {
    margin: 0;
    padding: 0;
    width: 1200px;
    height: 969px;
    overflow: hidden;
    background: var(--backdrop);
  }
  .stage {
    position: relative;
    width: 1200px;
    height: 969px;
  }
  .business-card {
    position: absolute;
    left: 100px;
    top: 190px;
    width: 1000px;
    height: 590px;
    filter: drop-shadow(0 18px 30px rgba(0,0,0,0.18));
  }
  .card-text {
    font-family: "Source Sans 3", sans-serif;
  }
  .holder-name { font-size: 37px; font-weight: 600; fill: var(--ink-light); }
  .contact-line { font-size: 24px; font-weight: 400; fill: var(--ink-light); }
  .address-line { font-size: 24px; font-weight: 400; fill: var(--gold-text); }
  .brand-vertical { font-size: 56px; font-weight: 700; fill: var(--ink-light); letter-spacing: 2px; }
  .brand-corner { font-size: 38px; font-weight: 700; fill: var(--ink-dark); letter-spacing: 2px; }
  .contact-icon { fill: none; stroke: var(--gold); stroke-width: 2; }
</style>
</head>
<body>
<main class="stage">
  <svg class="business-card" viewBox="0 0 1000 590" xmlns="http://www.w3.org/2000/svg" aria-label="Brindle Cases business card for Sam Ortiz">
    <defs>
      <clipPath id="card-shape">
        <rect x="0" y="0" width="1000" height="590" rx="28" ry="28"/>
      </clipPath>
      <linearGradient id="frost-fill" x1="0" y1="0" x2="1" y2="1">
        <stop offset="0" stop-color="var(--frost)"/>
        <stop offset="1" stop-color="var(--frost-shade)"/>
      </linearGradient>
      <radialGradient id="dark-fill" cx="0.45" cy="0.35" r="0.9">
        <stop offset="0" stop-color="var(--panel-dark-edge)"/>
        <stop offset="1" stop-color="var(--panel-dark)"/>
      </radialGradient>
      <linearGradient id="gold-band" x1="0" y1="0" x2="1" y2="0">
        <stop offset="0" stop-color="var(--gold-deep)"/>
        <stop offset="0.5" stop-color="var(--gold)"/>
        <stop offset="1" stop-color="var(--gold-light)"/>
      </linearGradient>
      <linearGradient id="gold-bevel" x1="0" y1="0" x2="0" y2="1">
        <stop offset="0" stop-color="var(--gold-light)"/>
        <stop offset="0.5" stop-color="var(--gold)"/>
        <stop offset="1" stop-color="var(--gold-deep)"/>
      </linearGradient>
    </defs>

    <g clip-path="url(#card-shape)">
      <!-- frosted base -->
      <rect class="card-frost" x="0" y="0" width="1000" height="590" fill="url(#frost-fill)"/>

      <!-- gold address band -->
      <rect class="address-band" x="430" y="184" width="570" height="227" fill="url(#gold-band)" opacity="0.85"/>

      <!-- gold bevel along dark panel edge -->
      <polygon class="panel-bevel" points="423,0 466,111 456,523 423,590 410,590 440,523 452,111 410,0" fill="url(#gold-bevel)"/>

      <!-- dark contact panel -->
      <polygon class="contact-panel" points="0,0 423,0 452,111 440,523 410,590 0,590" fill="url(#dark-fill)" opacity="0.95"/>
    </g>

    <!-- vertical brand name -->
    <text class="card-text brand-vertical" transform="translate(8,8) rotate(90)" x="0" y="0" dominant-baseline="hanging">BRINDLE CASES</text>

    <!-- holder -->
    <text class="card-text holder-name" x="117" y="214">Sam Ortiz</text>

    <!-- mobile -->
    <rect class="contact-icon" x="124" y="247" width="12" height="20" rx="2"/>
    <text class="card-text contact-line" x="163" y="265">027 481 2956</text>

    <!-- landline -->
    <path class="contact-icon" d="M121 302 q9 -8 18 0 M124 303 h12 l3 9 h-18 z" />
    <text class="card-text contact-line" x="163" y="308">09-527-3061</text>

    <!-- email -->
    <rect class="contact-icon" x="121" y="337" width="19" height="13"/>
    <path class="contact-icon" d="M121 337 l9.5 7 l9.5 -7"/>
    <text class="card-text contact-line" x="163" y="351">sales@brindlecases.co.nz</text>

    <!-- web -->
    <circle class="contact-icon" cx="130" cy="384" r="9"/>
    <path class="contact-icon" d="M121 384 h18 M130 375 q-6 9 0 18 M130 375 q6 9 0 18"/>
    <text class="card-text contact-line" x="163" y="393">www.brindlecases.co.nz</text>

    <!-- location pin -->
    <g class="pin-icon" transform="translate(732,257)">
      <circle cx="0" cy="0" r="20" fill="var(--ink-light)" opacity="0.75"/>
      <path d="M0 12 C-4 6 -8 2 -8 -3 A8 8 0 0 1 8 -3 C8 2 4 6 0 12 Z" fill="var(--gold)"/>
      <circle cx="0" cy="-3" r="3" fill="var(--ink-light)"/>
    </g>

    <!-- addresses -->
    <text class="card-text address-line" x="732" y="322" text-anchor="middle">3/17 Kestrel Lane, Morrow Flats, Auckland, 0614</text>
    <text class="card-text address-line" x="732" y="366" text-anchor="middle">PO Box 208354, North Shore, Auckland 0792</text>

    <!-- corner brand name -->
    <text class="card-text brand-corner" x="955" y="545" text-anchor="end">BRINDLE CASES</text>
  </svg>
</main>
</body>
</html>
```